Website homepage rework for women's travel website

I have a homepage (http://www.ladies-far-afield.example) that I'm 50% happy with but don't want to completely overhaul. I'd like to retain a similar look but upgrade it to something a bit more modern and less old-fashioned. The basic sense of the site is empowering, self-confident, fun and adventurous - but female and over 40.

A number of the elements on the page have to be redesigned, a few can be tweaked, and a few left alone. See the rest of the brief for further information.

Target Market(s)

women over 40 who like to travel

Industry/Entity Type

Travel

Number of Pages Required

1 page

Font styles to use
Other font styles liked:
• see my brief

Requirements
Must have
• - size - the page must be significantly wider
• - the only font I MUST keep is Raleway (as in the tagline) and possibly the font of the site name (Ladies Far Afield). Both of those work for me. There are too many fonts on the page, however, and that needs to be unified.
• - the rectangles I click to get inside the site have to change to something more modern, possibly square - they do not have to be separated into two columns as they are now, nor do they need the titles (toolkit etc)
• - I like the background image of the header - but it needs to be wider of course - also keep in mind the aspect - it has to fit into the smaller inside pages, whose size will not change
• - at the end of the project I need to receive the separate elements of the design so I can eventually make a change myself if needed ie. replace my own photo, for example
Nice to have
• - the three photos need to change to something more eye-popping - or something else should take their place to fill the space
Should not have
• I do not want a full, original redesign. I want my readers to still feel as though they are on the same site - same header, mostly same fonts.

```html
<!DOCTYPE html>
<html lang="en">
<head>
<meta charset="utf-8">
<title>Ladies Far Afield</title>
<link href="https://fonts.googleapis.com/css2?family=Raleway:wght@300;400;500;600&display=swap" rel="stylesheet">
<style>
:root{
  --ink:#2d2827;
  --text:#3a3a3a;
  --white:#ffffff;
  --muted:#b9b4b0;
  --accent:#f08a2c;
  --tile-orange:#e85a30;
  --tile-purple:#6a3bb5;
  --tile-amber:#ec7420;
  --tile-green:#389e2e;
  --tile-yellow:#ebb60c;
  --tile-teal:#21bd9a;
  --tile-red:#e5302c;
  --tile-blue:#2497de;
}
*{box-sizing:border-box;margin:0;padding:0}
html,body{width:1040px;height:1200px;overflow:hidden;background:var(--white)}
body{font-family:'Raleway',sans-serif;color:var(--text);position:relative}

.site-nav{height:50px;background:var(--ink);display:flex;align-items:center;justify-content:space-between;padding:0 78px 0 77px}
.brand{color:var(--white);font-size:20px;font-weight:500;letter-spacing:.3px}
.menu{display:flex;gap:31px;list-style:none;height:50px}
.menu li{display:flex;align-items:center;font-size:13px;color:var(--white);position:relative}
.menu li.active{color:var(--muted)}
.menu li.active::after{content:"";position:absolute;left:0;right:0;bottom:0;height:2px;background:var(--accent)}

.hero{position:relative;height:380px;overflow:hidden;
  background:linear-gradient(180deg,#f2a23a 0%,#f7c35a 30%,#e2a868 55%,#b97a4a 75%,#8a6650 100%)}
.hero-photo{position:absolute;inset:0;background:
  radial-gradient(ellipse 230px 300px at 210px 260px,rgba(205,200,180,.85),rgba(205,200,180,0) 70%),
  linear-gradient(90deg,rgba(0,0,0,0) 40%,rgba(0,0,0,0) 100%)}
.hero-title{position:absolute;left:392px;top:42px;width:577px;height:72px;
  background:linear-gradient(180deg,#f39a22,#e2561a);display:flex;align-items:center;justify-content:center;
  color:var(--white);font-size:50px;font-weight:500}
.hero-tagline{position:absolute;left:392px;top:120px;font-size:29px;font-weight:400;color:#2d2827}
.snapshots{position:absolute;left:528px;top:245px;display:flex;gap:8px}
.snapshot{width:130px;height:118px;background:#f4f1ec;padding:8px 8px 22px;box-shadow:0 2px 6px rgba(0,0,0,.3)}
.snapshot div{width:100%;height:100%}

.intro{text-align:center;padding-top:38px}
.intro-rule{width:34px;height:1px;background:#cfcfcf;margin:0 auto 12px}
.intro h1{font-size:20px;font-weight:400;color:var(--text)}

.pillars{display:flex;justify-content:center;gap:55px;margin-top:22px}
.pillar{width:240px;text-align:center}
.pillar svg{height:32px;display:block;margin:0 auto 10px}
.pillar h2{font-size:17px;font-weight:600;color:var(--ink);margin-bottom:6px}
.pillar p{font-size:12px;line-height:18px;font-weight:400;color:var(--text)}

.cta-band{position:absolute;left:0;top:672px;width:1040px;height:54px;background:var(--ink);
  display:flex;align-items:center;justify-content:center;color:var(--white);font-size:16px;font-weight:500}

.tiles{position:absolute;left:77px;top:760px;width:885px;display:grid;grid-template-columns:repeat(4,1fr);gap:2px}
.tile{height:186px;display:flex;flex-direction:column}
.tile-head{height:83px;padding:16px 16px 0;color:var(--white)}
.tile-head small{display:block;font-size:10px;font-weight:500;margin-bottom:6px}
.tile-head strong{display:block;font-size:15px;font-weight:500;line-height:17px}
.tile-img{flex:1}
.t-orange .tile-head{background:var(--tile-orange)}
.t-purple .tile-head{background:var(--tile-purple)}
.t-amber .tile-head{background:var(--tile-amber)}
.t-green .tile-head{background:var(--tile-green)}
.t-yellow .tile-head{background:var(--tile-yellow)}
.t-teal .tile-head{background:var(--tile-teal)}
.t-red .tile-head{background:var(--tile-red)}
.t-blue .tile-head{background:var(--tile-blue)}

.site-footer{position:absolute;left:0;bottom:0;width:1040px;height:39px;background:var(--ink);color:var(--white);
  display:flex;align-items:center;justify-content:space-between;padding:0 76px 0 78px;font-size:12px}
.legal{display:flex;gap:14px}
</style>
</head>
<body>
<nav class="site-nav">
  <div class="brand">Ladies Far Afield</div>
  <ul class="menu">
    <li class="active">Start Here</li>
    <li>About</li>
    <li>Travel Resources</li>
    <li>Blog</li>
    <li>Travel Shop</li>
    <li>Contact</li>
  </ul>
</nav>

<header class="hero">
  <div class="hero-photo" role="img" aria-label="Portrait of the smiling site author in a light shirt, set against a desert road with red rock buttes and an old map"></div>
  <div class="hero-title">Ladies Far Afield</div>
  <div class="hero-tagline">For women who travel smart, safe + solo</div>
  <div class="snapshots">
    <div class="snapshot"><div role="img" aria-label="Beach with palm trees and blue sea" style="background:linear-gradient(180deg,#4aa3d8,#2b6f9a 60%,#6b5b3a)"></div></div>
    <div class="snapshot"><div role="img" aria-label="Blue pots with agave plants against a terracotta wall" style="background:linear-gradient(160deg,#d8824a,#3a8fc7 60%,#5d8a3a)"></div></div>
    <div class="snapshot"><div role="img" aria-label="Red scooter parked on a street with plants" style="background:linear-gradient(180deg,#c9a27a,#6f8f5a 55%,#c0392b)"></div></div>
  </div>
</header>

<section class="intro">
  <div class="intro-rule"></div>
  <h1>Hi, I'm Marta. I took my first solo trip at 15. I'll show you how to travel</h1>
  <div class="pillars">
    <div class="pillar">
      <svg viewBox="0 0 34 32" aria-hidden="true"><circle cx="11" cy="9" r="6" fill="#2d2827"/><path d="M1 32v-8c0-4 4-7 10-7s10 3 10 7v8z" fill="#2d2827"/><path d="M11 18l-2 6 2 5 2-5z" fill="#fff"/><circle cx="26" cy="10" r="5" fill="#2d2827"/><rect x="24" y="15" width="4" height="4" fill="#2d2827"/><path d="M26 1v2M33 9h-2M19 9h2M31 4l-1.5 1.5M21 4l1.5 1.5" stroke="#2d2827" stroke-width="1.5"/></svg>
      <h2>Smart</h2>
      <p>Practical tools to help you plan - and afford - the perfect trip.</p>
    </div>
    <div class="pillar">
      <svg viewBox="0 0 32 34" aria-hidden="true"><path d="M14 1l13 5v10c0 9-6 14-13 17C7 30 1 25 1 16V6z" fill="#2d2827"/><circle cx="25" cy="26" r="6" fill="#fff"/><path d="M21 26l3 3 6-6" stroke="#2d2827" stroke-width="2" fill="none"/></svg>
      <h2>Safe</h2>
      <p>Practical tools to help you plan - and afford - the perfect trip.</p>
    </div>
    <div class="pillar">
      <svg viewBox="0 0 20 32" aria-hidden="true"><path d="M5 9l8-7v28" stroke="#2d2827" stroke-width="2.2" fill="none" stroke-linecap="round"/></svg>
      <h2>Solo</h2>
      <p>Practical tools to help you plan - and afford - the perfect trip.</p>
    </div>
  </div>
</section>

<div class="cta-band">Thinking of solo travel? CLICK HERE to find out how</div>

<main class="tiles">
  <article class="tile t-orange"><div class="tile-head"><small>Eating with locals</small><strong>The ultimate guide to social dining</strong></div><div class="tile-img" role="img" aria-label="Salad with oranges and vegetables on a dark wooden table" style="background:linear-gradient(135deg,#3b2e25,#6a4a2e 50%,#2f2620)"></div></article>
  <article class="tile t-purple"><div class="tile-head"><small>Your Packing List</small><strong>Take what you need - no more</strong></div><div class="tile-img" role="img" aria-label="Open notebook with a pencil beside a camera" style="background:linear-gradient(135deg,#d6cfc2,#a89a86 55%,#3a3430)"></div></article>
  <article class="tile t-amber"><div class="tile-head"><small>No Single Supplement</small><strong>17 ways to avoid paying it</strong></div><div class="tile-img" role="img" aria-label="Orange sunset behind dark rock silhouettes" style="background:linear-gradient(180deg,#c5641c,#8a3c12 55%,#1e140f)"></div></article>
  <article class="tile t-green"><div class="tile-head"><small>Stress Management Courses</small><strong>How to travel stress-free</strong></div><div class="tile-img" role="img" aria-label="Shirts and jackets hanging on a clothes rail" style="background:linear-gradient(90deg,#eceae6,#9aa3ad 50%,#e8e6e2)"></div></article>
  <article class="tile t-yellow"><div class="tile-head"><small>Solo In Argentina</small><strong>Does it really take two to tango</strong></div><div class="tile-img" role="img" aria-label="Blue lake between forested hills" style="background:linear-gradient(180deg,#5b9ad0,#1f5f9a 50%,#1f3a22)"></div></article>
  <article class="tile t-teal"><div class="tile-head"><small>Europe For Foodies</small><strong>9 top destinations to try in October</strong></div><div class="tile-img" role="img" aria-label="Platter of cheese, cured ham, olives and bread" style="background:linear-gradient(135deg,#4a3a2c,#d9c49a 50%,#8a5040)"></div></article>
  <article class="tile t-red"><div class="tile-head"><small>Solo Female Travel</small><strong>A 3-Week Central Asia itinerary</strong></div><div class="tile-img" role="img" aria-label="Tiled madrasa facade with arched portal under blue sky" style="background:linear-gradient(180deg,#7aa8d8,#a07a52 45%,#6a4a30)"></div></article>
  <article class="tile t-blue"><div class="tile-head"><small>Rebellious Carouge</small><strong>Geneva's Alter Ego?</strong></div><div class="tile-img" role="img" aria-label="Pale green camper van parked by a beach" style="background:linear-gradient(180deg,#5fb8d8,#b8d4b0 50%,#d8c8a8)"></div></article>
</main>

<footer class="site-footer">
  <div>© Ladies Far Afield</div>
  <div class="legal"><span>Privacy Policy</span><span>|</span><span>Terms &amp; Conditions</span></div>
</footer>
</body>
</html>
```